A website for a Maltese Law Firm

Our law firm needs a website to further its business. The site should have a simple yet effective design. We would need the following sections: About us, Practice Areas, About Malta, Contact. These should be further split as follows:

About us: Our firm, Our values, What others say, Offices

Practice Areas: Crimimal, Citizenship & Residence, Harbour Passage Scheme, Criminal Defence, Civil Litigation, Arbitration and ADR, Commercial and Corporate, Media Law.

About Malta: just one section.

Contact: Just one section

We would also need a news feed at the front of the site to include latest news regarding our cases.

At the bottom we need a section for our Terms and a Privacy Statement.

Our logo is being attached.

Target Market(s)

All clients looking for legal assistance in Malta

Industry/Entity Type

Legal

Coding

Coded - Design and coding required

Number of Pages Required

1 page

Requirements
Must have
• It must be simple yet striking.

```html
<!DOCTYPE html>
<html lang="en">
<head>
<meta charset="utf-8">
<title>Marlow &amp; Seren Advocates</title>
<link href="https://fonts.googleapis.com/css2?family=Lora:wght@400;500&family=Open+Sans:wght@400;600&display=swap" rel="stylesheet">
<style>
:root{
  --ink:#1e1e1e;
  --text:#333333;
  --muted:#7a7a7a;
  --light:#f2f2f2;
  --line:#d6d6d6;
  --white:#ffffff;
  --dark:#232323;
  --darker:#141414;
  --serif:'Lora', Georgia, serif;
  --sans:'Open Sans', Arial, sans-serif;
}
*{box-sizing:border-box;margin:0;padding:0}
html,body{width:1200px;height:2667px;overflow:hidden}
body{background:var(--white);font-family:var(--sans);color:var(--text);position:relative}
a{color:inherit;text-decoration:none}

.site-header{position:absolute;top:0;left:0;width:1200px;height:55px;background:var(--white)}
.brand{position:absolute;left:89px;top:12px;font-family:var(--serif);font-size:21px;letter-spacing:1px;color:var(--ink);border-bottom:1px solid var(--ink);padding-bottom:2px}
.main-nav{position:absolute;right:88px;top:19px;display:flex;gap:32px;font-size:14px;color:var(--ink)}

.hero{position:absolute;top:55px;left:0;width:1200px;height:517px;background:linear-gradient(180deg,#3a3a3a 0%,#2a2a2a 45%,#1c1c1c 100%)}
.hero-photo{position:absolute;inset:0;background:radial-gradient(ellipse at 50% 35%,rgba(120,120,120,.35),rgba(0,0,0,0) 60%)}
.hero-title{position:absolute;left:262px;top:232px;width:676px;text-align:center;color:var(--white)}
.hero-title .rule{height:1px;background:rgba(255,255,255,.85)}
.hero-title h1{font-family:var(--serif);font-weight:400;font-size:44px;letter-spacing:2px;margin:10px 0 4px;line-height:1.1}
.hero-title .sub{display:flex;align-items:center;gap:14px;font-family:var(--serif);font-size:16px;letter-spacing:2px}
.hero-title .sub span.rule{flex:1}

.about{position:absolute;top:572px;left:0;width:1200px;height:393px}
.section-title{font-family:var(--serif);font-weight:400;font-size:34px;color:var(--ink);text-align:center}
.about .section-title{margin-top:26px}
.about .intro{width:480px;margin:8px auto 0;text-align:center;font-size:13px;line-height:21px}
.about-grid{position:absolute;left:107px;top:142px;display:grid;grid-template-columns:506px 470px;row-gap:32px}
.about-item{display:flex;gap:20px}
.about-item svg{width:36px;height:36px;flex:none;margin-top:2px}
.about-item h3{font-family:var(--serif);font-weight:400;font-size:22px;color:var(--ink);line-height:26px}
.about-item p{font-size:11.5px;line-height:19px;width:410px;margin-top:2px}

.practice{position:absolute;top:965px;left:0;width:1200px;height:404px;background:var(--light);border-top:1px solid var(--line)}
.practice .section-title{margin-top:26px}
.tile{position:absolute;top:84px;width:246px;height:270px}
.tile .photo{width:100%;height:100%}
.tile .label{position:absolute;left:16px;bottom:-14px;width:214px;height:42px;background:var(--ink);color:var(--white);font-family:var(--serif);font-size:16px;display:flex;align-items:center;justify-content:center}

.malta{position:absolute;top:1369px;left:0;width:1200px;height:311px}
.malta .photo{position:absolute;left:0;top:0;width:555px;height:311px;background:linear-gradient(180deg,#d9e3ea 0%,#d8b98a 48%,#a8845a 66%,#2f4a6a 78%,#1d3352 100%)}
.malta .panel{position:absolute;left:555px;top:0;width:645px;height:311px;background:linear-gradient(90deg,#2e2e2e,#3a3a3a);color:var(--white);padding:44px 90px 0 46px}
.malta h2{font-family:var(--serif);font-weight:400;font-size:26px;margin-bottom:12px}
.malta p{font-size:12px;line-height:19.5px;margin-bottom:10px}

.news{position:absolute;top:1680px;left:0;width:1200px;height:391px}
.news .section-title{font-size:28px;margin-top:34px}
.post .photo{position:absolute;width:226px;height:224px;top:1778px}
.post .date{position:absolute;top:1778px;width:53px;height:71px;background:var(--ink);color:var(--white);text-align:center;font-size:19px;line-height:28px;padding-top:6px}
.post .date span{display:block;font-size:16px}
.post .card{position:absolute;top:1760px;width:250px;height:258px;background:var(--white);border:1px solid var(--line);padding:60px 30px 0 32px}
.card .place{font-size:11.5px;color:var(--muted)}
.card h3{font-family:var(--serif);font-weight:400;font-size:17px;color:var(--ink);margin-top:2px}
.card .bar{width:13px;height:2px;background:var(--ink);margin:6px 0 10px}
.card p{font-size:11.5px;line-height:18.5px}
.card .comments{font-size:12px;margin-top:12px}

.contact{position:absolute;top:2071px;left:0;width:1200px;height:393px;background:var(--light);border-top:1px solid var(--line)}
.contact .section-title{font-size:28px;margin-top:30px}
.field{position:absolute;background:var(--white);border:1px solid var(--line);font-size:13px;color:var(--muted);padding:10px 20px}
.send{position:absolute;left:533px;top:306px;width:134px;height:37px;background:var(--ink);color:var(--white);font-size:14px;display:flex;align-items:center;justify-content:center}

.site-footer{position:absolute;top:2464px;left:0;width:1200px;height:156px;background:var(--dark);color:var(--white)}
.site-footer .brand{position:static;display:block;width:max-content;margin:44px auto 0;color:var(--white);border-bottom:1px solid var(--white);font-size:24px}
.footer-nav{display:flex;justify-content:center;gap:34px;font-size:13.5px;margin-top:18px}
.legal{position:absolute;top:2620px;left:0;width:1200px;height:47px;background:var(--darker);color:var(--white);font-size:11.5px}
.legal .copy{position:absolute;left:89px;top:16px}
.legal .links{position:absolute;right:89px;top:16px}
</style>
</head>
<body>

<header class="site-header">
  <div class="brand">MARLOW &amp; SEREN</div>
  <nav class="main-nav">
    <a href="#">Home</a><a href="#">About us</a><a href="#">Practice Areas</a><a href="#">About Malta</a><a href="#">Contact</a>
  </nav>
</header>

<section class="hero" role="img" aria-label="Dark courtroom interior with benches and hanging lamp">
  <div class="hero-photo"></div>
  <div class="hero-title">
    <div class="rule"></div>
    <h1>WHEN EXPERIENCE MATTERS</h1>
    <div class="sub"><span class="rule"></span>MARLOW &amp; SEREN ADVOCATES<span class="rule"></span></div>
  </div>
</section>

<section class="about">
  <h2 class="section-title">About Us</h2>
  <p class="intro">Lorem ipsum dolor sit amet, consectetuer adipiscing elit. Aenean commodo ligula eget dolor. Cum sociis natoque penatibus et .</p>
  <div class="about-grid">
    <div class="about-item">
      <svg viewBox="0 0 36 36"><path d="M18 3 3 11h30z" fill="#1e1e1e"/><rect x="4" y="12" width="28" height="3" fill="#1e1e1e"/><rect x="7" y="16" width="4" height="12" fill="#1e1e1e"/><rect x="16" y="16" width="4" height="12" fill="#1e1e1e"/><rect x="25" y="16" width="4" height="12" fill="#1e1e1e"/><rect x="3" y="29" width="30" height="4" fill="#1e1e1e"/></svg>
      <div><h3>Our firm</h3><p>Lorem ipsum dolor sit amet, consectetuer adipiscing elit. Aenean commodo ligula eget dolor enean massa. Cum sociis natoque penatibus et magnis dis parturient montes, nascetur ridiculus mus.</p></div>
    </div>
    <div class="about-item">
      <svg viewBox="0 0 36 36"><path d="M2 14 10 7l8 4 8-4 8 7-6 6-10 10-4-3-12-9z" fill="#1e1e1e"/><path d="M12 18l4 4M15 15l5 5M18 13l5 5" stroke="#fff" stroke-width="1.5"/></svg>
      <div><h3>Our values</h3><p>Lorem ipsum dolor sit amet, consectetuer adipiscing elit. Aenean commodo ligula eget dolor enean massa. Cum sociis natoque penatibus et magnis dis parturient montes, nascetur ridiculus mus.</p></div>
    </div>
    <div class="about-item">
      <svg viewBox="0 0 36 36"><circle cx="18" cy="16" r="12" fill="#1e1e1e"/><path d="M9 24 6 32l9-5z" fill="#1e1e1e"/><rect x="12" y="12" width="12" height="2" fill="#fff"/><rect x="12" y="17" width="9" height="2" fill="#fff"/></svg>
      <div><h3>What others say</h3><p>Lorem ipsum dolor sit amet, consectetuer adipiscing elit. Aenean commodo ligula eget dolor enean massa. Cum sociis natoque penatibus et magnis dis parturient montes, nascetur ridiculus mus.</p></div>
    </div>
    <div class="about-item">
      <svg viewBox="0 0 36 36"><rect x="3" y="10" width="13" height="23" fill="#1e1e1e"/><rect x="17" y="3" width="16" height="30" fill="#1e1e1e"/><g fill="#fff"><rect x="6" y="14" width="3" height="3"/><rect x="10" y="14" width="3" height="3"/><rect x="6" y="20" width="3" height="3"/><rect x="10" y="20" width="3" height="3"/><rect x="20" y="7" width="3" height="3"/><rect x="27" y="7" width="3" height="3"/><rect x="20" y="14" width="3" height="3"/><rect x="27" y="14" width="3" height="3"/><rect x="20" y="21" width="3" height="3"/><rect x="27" y="21" width="3" height="3"/></g></svg>
      <div><h3>Offices</h3><p>Lorem ipsum dolor sit amet, consectetuer adipiscing elit. Aenean commodo ligula eget dolor enean massa. Cum sociis natoque penatibus et magnis dis parturient montes, nascetur ridiculus mus.</p></div>
    </div>
  </div>
</section>

<section class="practice">
  <h2 class="section-title">Practice Areas</h2>
  <div class="tile" style="left:89px"><div class="photo" role="img" aria-label="Handgun lying in dry grass" style="background:linear-gradient(180deg,#c9b79a,#8f7a54 60%,#5a6a3a)"></div><div class="label">Criminal Defence</div></div>
  <div class="tile" style="left:347px"><div class="photo" role="img" aria-label="Press cameras and crowd at a media event" style="background:linear-gradient(135deg,#2a2a30,#8a4b3a 45%,#c9a08a 70%,#6a6a6a)"></div><div class="label">Media Law</div></div>
  <div class="tile" style="left:606px"><div class="photo" role="img" aria-label="Judge's gavel resting on law books on a wooden desk" style="background:linear-gradient(160deg,#b98a5a,#3a4a5a 45%,#8a5a3a 75%,#c49a6a)"></div><div class="label">Civil Litigation</div></div>
  <div class="tile" style="left:866px"><div class="photo" role="img" aria-label="Hands in handcuffs" style="background:linear-gradient(160deg,#2a2a2a,#8a6a55 50%,#3a3a3a)"></div><div class="label">Criminal</div></div>
</section>

<section class="malta">
  <div class="photo" role="img" aria-label="Valletta skyline with domed church across the harbour at sunset"></div>
  <div class="panel">
    <h2>About Malta</h2>
    <p>Lorem ipsum dolor sit amet, consectetuer adipiscing elit. Aenean commodo ligula eget dolor. Aenean massa. Cum sociis natoque penatibus et magnis dis parturient montes, nascetur ridiculus mus. Donec quam felis, ultricies nec, pellentesque eu, pretium quis, sem. Nulla consequat massa quis enim. Donec pede justo, fringilla vel, aliquet nec, vulputate eget, arcu. In enim justo, rhoncus .</p>
    <p>Aenean com+modo ligula eget dolor. Aenean massa. Cum sociis natoque penatibus et magnis dis parturient montes, nascetur ridiculus mus. Donec quam felis, ultricies nec, pellentesque eu, pretium quis, sem.</p>
  </div>
</section>

<section class="news">
  <h2 class="section-title">Latest News</h2>
</section>
<article class="post">
  <div class="photo" role="img" aria-label="Stone courthouse building under blue sky with flag" style="left:89px;background:linear-gradient(180deg,#6fa3d8 0%,#a9c9e8 40%,#d8cfae 60%,#8a7f62 100%)"></div>
  <div class="date" style="left:89px">Jun<span>07</span></div>
  <div class="card" style="left:315px">
    <div class="place">New York, United states</div>
    <h3>In The Court of law</h3>
    <div class="bar"></div>
    <p>Lorem ipsum dolor sit amet, consectetuer adipiscing elit. Aenean commodo ligula eget dolor. Cum sociis natoque penatibus et magnis Lorem ipsum d.</p>
    <div class="comments">3 comments</div>
  </div>
</article>
<article class="post">
  <div class="photo" role="img" aria-label="Law library hall with book-lined walls and long tables" style="left:610px;background:linear-gradient(180deg,#c9b89a 0%,#7a5a3a 45%,#2e3438 80%,#1e2428 100%)"></div>
  <div class="date" style="left:610px">Jun<span>07</span></div>
  <div class="card" style="left:834px;width:277px">
    <div class="place">New York, United states</div>
    <h3>Money Laundering</h3>
    <div class="bar"></div>
    <p>Lorem ipsum dolor sit amet, consectetuer adipiscing elit. Aenean commodo ligula eget dolor. Cum sociis natoque penatibus et magnis Lorem ipsum d.</p>
    <div class="comments">3 comments</div>
  </div>
</article>

<section class="contact">
  <h2 class="section-title">Contact Us</h2>
  <div class="field" style="left:210px;top:80px;width:382px;height:40px">Name*</div>
  <div class="field" style="left:601px;top:80px;width:382px;height:40px">Email*</div>
  <div class="field" style="left:210px;top:128px;width:382px;height:41px">Subject*</div>
  <div class="field" style="left:601px;top:128px;width:382px;height:41px">Phone*</div>
  <div class="field" style="left:210px;top:178px;width:773px;height:148px">Message*</div>
  <div class="send">Send</div>
</section>

<footer class="site-footer">
  <div class="brand">MARLOW &amp; SEREN</div>
  <nav class="footer-nav">
    <a href="#">Home</a><a href="#">About us</a><a href="#">Practice Areas</a><a href="#">About Malta</a><a href="#">Contact</a>
  </nav>
</footer>
<div class="legal">
  <div class="copy">Copyright 2016 | All Right Reserved</div>
  <div class="links">Terms &amp; Conditions | Privacy Policy</div>
</div>

</body>
</html>
```